General Contractor in Construction and Low Voltage

This is my 2nd time doing a mosaic hive. I currently have a wordpress website. The first time around I got a bunch of great ideas that are still implemented into my current website but I had to add the construction portion recently and now it feels really cluttered and inconsistent. I'm looking to update my current website into a more professional website theme based off the current ideas, pictures, and wordage already on my website. My company is called Tessaridge.com based off my time in the Corvants and being a veteran and for my son. I would like that to be part of my theme. I would prefer a Blue like the current but I need some more ideas with pictures and the layout. I do like the majority of my layout but I don't think the theme is all together and my home page just sucks. The final design should communicate professional and modern.

```html
<!DOCTYPE html>
<html lang="en">
<head>
<meta charset="UTF-8">
<title>Tessaridge General Contractor</title>
<link href="https://fonts.googleapis.com/css2?family=Oswald:wght@500;600&family=Lato:wght@400;700&display=swap" rel="stylesheet">
<style>
:root{
  --navy:#002a78;
  --navy-dark:#001b52;
  --topbar:#001a4d;
  --ink:#1d1d1d;
  --body:#333;
  --soft:#f4f5f7;
  --footer:#1c1c1e;
  --white:#fff;
}
*{box-sizing:border-box;margin:0;padding:0}
html,body{width:1200px;height:3244px;overflow:hidden}
body{font-family:'Lato',sans-serif;color:var(--body);background:var(--white);position:relative}
.head{font-family:'Oswald',sans-serif;font-weight:600;text-transform:uppercase;color:var(--ink)}
.eyebrow{font-size:12px;letter-spacing:1.2px;text-transform:uppercase;color:var(--navy)}
.wrap{position:absolute;left:161px;width:878px}

.topbar{position:absolute;top:0;left:0;width:1200px;height:35px;background:var(--topbar);color:#fff;font-size:12px}
.topbar .items{position:absolute;right:161px;top:10px;display:flex;gap:36px;align-items:center}
.topbar .items span{display:flex;gap:8px;align-items:center}
.site-header{position:absolute;top:35px;left:0;width:1200px;height:112px;background:var(--navy)}
.brand{position:absolute;left:161px;top:38px;display:flex;align-items:center;gap:10px;color:#fff;font-family:'Oswald',sans-serif;font-weight:500;font-size:22px;letter-spacing:2px}
.brand i{width:14px;height:14px;background:#fff;display:block}
.nav{position:absolute;right:161px;top:46px;display:flex;gap:35px;font-family:'Oswald',sans-serif;font-weight:500;font-size:14px;color:#fff;text-transform:uppercase}
.nav .on{text-decoration:underline;text-underline-offset:4px;font-weight:600}

.hero{position:absolute;top:147px;left:0;width:1200px;height:675px;background:linear-gradient(120deg,#8b7c62 0%,#b79a5e 30%,#d8c48a 55%,#c9b060 75%,#8a7a5a 100%)}
.hero::after{content:"";position:absolute;inset:0;background:rgba(10,20,50,.35)}
.hero .txt{position:absolute;z-index:1;top:160px;left:0;width:1200px;text-align:center;color:#fff}
.hero .eyebrow{color:#fff;font-size:13px}
.hero h1{font-family:'Oswald',sans-serif;font-weight:600;font-size:56px;line-height:60px;margin-top:18px;text-transform:uppercase}
.hero p{font-size:13px;line-height:24px;width:500px;margin:34px auto 0}
.btn-white{display:inline-block;background:#fff;color:var(--navy);font-family:'Oswald',sans-serif;font-weight:600;font-size:13px;text-transform:uppercase;padding:14px 29px}
.hero .btn-white{margin-top:40px}

.features{top:747px;height:150px;display:flex;background:var(--navy);z-index:2}
.feature{flex:1;padding:30px 16px 0 78px;position:relative;color:#fff;border-right:1px solid rgba(255,255,255,.25)}
.feature:last-child{border:none}
.feature svg{position:absolute;left:22px;top:52px}
.feature h3{font-family:'Oswald',sans-serif;font-weight:500;font-size:16px;text-transform:uppercase}
.feature p{font-size:11.5px;line-height:22px;margin-top:8px}

.about{top:968px}
.about h2{font-size:29px;margin-top:6px}
.about p{font-size:12.5px;line-height:22.5px;width:352px;margin-top:26px}
.about p+p{margin-top:10px}
.btn-navy{display:inline-block;background:var(--navy);color:#fff;font-family:'Oswald',sans-serif;font-weight:600;font-size:13px;text-transform:uppercase;padding:14px 31px}
.about .btn-navy{margin-top:26px}
.about-mark{position:absolute;left:520px;top:8px;width:358px;height:330px;display:flex;flex-direction:column;align-items:center;justify-content:center;gap:22px}
.about-mark span{font-family:'Oswald',sans-serif;font-weight:600;font-size:50px;color:var(--navy);letter-spacing:3px}
.about-mark i{width:66px;height:66px;border-radius:50%;background:var(--navy);display:block}

.services{position:absolute;top:1384px;left:0;width:1200px;height:555px;background:var(--soft);text-align:center}
.services .eyebrow{margin-top:74px}
.services h2{font-size:29px;margin-top:4px}
.svc{position:absolute;top:157px;width:428px;height:275px}
.svc .photo{width:100%;height:100%}
.svc .cap{position:absolute;left:76px;top:228px;width:276px;height:92px;background:#fff;box-shadow:0 2px 6px rgba(0,0,0,.08);padding-top:16px}
.svc .cap h3{font-family:'Oswald',sans-serif;font-weight:500;font-size:16px;color:var(--navy);text-transform:uppercase}
.svc .cap b{display:block;width:26px;height:26px;border-radius:50%;background:var(--navy);margin:8px auto 0;position:relative}

.cta{position:absolute;top:1939px;left:0;width:1200px;height:232px;background:linear-gradient(90deg,#002a78 0%,#0a3590 60%,#234a9c 100%)}
.cta h2{position:absolute;left:186px;top:68px;font-family:'Oswald',sans-serif;font-weight:600;font-size:28px;color:#fff;text-transform:uppercase}
.cta p{position:absolute;left:187px;top:116px;width:560px;font-size:12.5px;line-height:24px;color:#fff}
.cta .btn-white{position:absolute;left:913px;top:94px;padding:14px 34px}

.markets{top:2232px;text-align:center}
.markets h2{font-size:29px;margin-top:4px}
.market-row{display:flex;gap:23px;margin-top:28px}
.market{width:277px;height:368px;background:var(--navy);color:#fff}
.market .photo{height:217px}
.market h3{font-family:'Oswald',sans-serif;font-weight:500;font-size:17px;text-transform:uppercase;margin-top:22px}
.market hr{width:30px;border:none;border-top:1px solid rgba(255,255,255,.6);margin:12px auto 14px}
.market p{font-size:11.5px;line-height:21px;padding:0 26px}
.markets .more{display:inline-block;margin-top:54px;font-size:11.5px;color:var(--ink);text-decoration:underline}

.site-footer{position:absolute;top:2843px;left:0;width:1200px;height:401px;background:var(--footer);color:#fff}
.foot-brand{position:absolute;left:161px;top:90px;display:flex;align-items:center;gap:10px;font-family:'Oswald',sans-serif;font-weight:500;font-size:22px;letter-spacing:2px}
.foot-brand i{width:14px;height:14px;background:#fff;display:block}
.foot-rule{position:absolute;left:161px;top:172px;width:202px;border-top:1px solid #3a3a3a}
.follow{position:absolute;left:161px;top:202px;display:flex;gap:10px;align-items:center;font-size:12px}
.follow i{width:26px;height:26px;background:#fff;display:block}
.follow span{margin-right:4px}
.fcol{position:absolute;top:72px}
.fcol h4{font-family:'Oswald',sans-serif;font-weight:600;font-size:19px;text-transform:uppercase}
.fcol .bar{width:38px;border-top:2px solid var(--navy);margin:12px 0 16px}
.links li{list-style:none;font-size:11.5px;line-height:27px}
.contact li{list-style:none;display:flex;align-items:center;gap:12px;font-size:11.5px;margin-bottom:23px}
.contact b{width:33px;height:33px;background:#333;display:flex;align-items:center;justify-content:center}
.copy{position:absolute;top:372px;left:0;width:1200px;text-align:center;font-family:'Oswald',sans-serif;font-weight:500;font-size:12px}
</style>
</head>
<body>

<div class="topbar">
  <div class="items">
    <span><svg width="11" height="11" viewBox="0 0 24 24"><path fill="#fff" d="M6.6 10.8a15 15 0 006.6 6.6l2.2-2.2c.3-.3.7-.4 1-.2 1.1.4 2.3.6 3.6.6.6 0 1 .4 1 1V20c0 .6-.4 1-1 1A17 17 0 013 4c0-.6.4-1 1-1h3.5c.6 0 1 .4 1 1 0 1.3.2 2.5.6 3.6.1.3 0 .7-.2 1z"/></svg>555-014-2290</span>
    <span style="opacity:.4">|</span>
    <span><svg width="12" height="9" viewBox="0 0 24 18"><rect width="24" height="18" fill="#fff"/><path d="M0 0l12 9 12-9" stroke="#001a4d" stroke-width="2" fill="none"/></svg>support@tessaridge.com</span>
  </div>
</div>

<header class="site-header">
  <div class="brand"><i></i>TESSARIDGE</div>
  <nav class="nav">
    <span class="on">Home</span><span>Construction</span><span>Low Woltage</span><span>Markets</span><span>Our Team</span><span>Contact</span>
  </nav>
</header>

<section class="hero" role="img" aria-label="Photo of blueprints, a tool belt, work gloves and a yellow hard hat on a wooden table">
  <div class="txt">
    <div class="eyebrow">Welcome to Tessaridge</div>
    <h1>From initial concept<br>to final construction</h1>
    <p>Lorem ipsum dolor sit amet, consectetur adipiscing elit, sed do eiusmod tempor incididunt ut labore et dolore magna aliqua. Ut enim ad minim veniam, quis nostrud exercitation ullamco.</p>
    <span class="btn-white">Our Services</span>
  </div>
</section>

<div class="wrap features">
  <div class="feature">
    <svg width="42" height="42" viewBox="0 0 42 42" fill="none" stroke="#fff" stroke-width="1.5"><circle cx="21" cy="21" r="13"/><circle cx="21" cy="21" r="6"/><path d="M21 2v6M21 34v6M2 21h6M34 21h6M7.6 7.6l4.2 4.2M30.2 30.2l4.2 4.2M7.6 34.4l4.2-4.2M30.2 11.8l4.2-4.2"/></svg>
    <h3>Experience</h3>
    <p>Our past projects include both new construction and repairs/restorations. And we can also plan &amp; design jobs.</p>
  </div>
  <div class="feature">
    <svg width="42" height="42" viewBox="0 0 42 42" fill="none" stroke="#fff" stroke-width="1.5"><rect x="4" y="4" width="34" height="34" rx="4"/><circle cx="21" cy="21" r="9"/><circle cx="21" cy="21" r="3"/></svg>
    <h3>Client Support</h3>
    <p>We offer an end-to-end client experience that includes seamless communication, budgeting, quality.</p>
  </div>
  <div class="feature">
    <svg width="46" height="42" viewBox="0 0 46 42" fill="none" stroke="#fff" stroke-width="1.5"><path d="M2 14l10-6 10 6 10-6 12 6M8 18l14 14 6-4 10-12"/><path d="M18 24l4 4M22 20l4 4"/></svg>
    <h3>Trust</h3>
    <p>We are committed to building trust among our clients, contractors, colleagues, and community.</p>
  </div>
</div>

<section class="wrap about">
  <div class="eyebrow">Welcome to Tessaridge</div>
  <h2 class="head">About the owner</h2>
  <p>Dale was honorably discharged from the Corvants Corps in 2005 and was awarded the purple heart from the wounds received in Iraq. Dale has over 20 years of experience in the low-voltage &amp; construction industries with a focus on general contracting and project management</p>
  <p>He works tirelessly to service commercial, industrial and government clients with the type of ingenuity resourcefulness and preserverance that are espeacialy unique to military veterans</p>
  <span class="btn-navy">Read More</span>
  <div class="about-mark"><span>TESSARIDGE</span><i></i></div>
</section>

<section class="services">
  <div class="eyebrow">What we offer</div>
  <h2 class="head">Services</h2>
  <div class="svc" style="left:161px">
    <div class="photo" role="img" aria-label="Photo of a tape measure, level and hard hat on construction drawings" style="background:linear-gradient(135deg,#d9c24a 0%,#e9e6dc 40%,#f3f1ea 70%,#cfd3d9 100%)"></div>
    <div class="cap"><h3>Construction</h3><b><svg width="26" height="26" viewBox="0 0 26 26"><path d="M8 13h10M14 9l4 4-4 4" stroke="#fff" stroke-width="1.5" fill="none"/></svg></b></div>
  </div>
  <div class="svc" style="left:611px">
    <div class="photo" role="img" aria-label="Photo of an electrician with a tool belt working on low voltage wiring" style="background:linear-gradient(90deg,#e6e7ea 0%,#8a7560 35%,#3a4f96 50%,#d9dbdf 70%,#c9ccd3 100%)"></div>
    <div class="cap"><h3>Low Voltage</h3><b><svg width="26" height="26" viewBox="0 0 26 26"><path d="M8 13h10M14 9l4 4-4 4" stroke="#fff" stroke-width="1.5" fill="none"/></svg></b></div>
  </div>
</section>

<section class="cta">
  <h2>Got any project you would like to discuss?</h2>
  <p>Lorem ipsum dolor sit amet, consectetur adipiscing elit, sed do eiusmod tempor incididunt ut labore et dolore magna aliqua. Ut enim ad minim veniam.</p>
  <span class="btn-white">Contact Us</span>
</section>

<section class="wrap markets">
  <div class="eyebrow">Trusted service provider</div>
  <h2 class="head">Our Markets</h2>
  <div class="market-row">
    <div class="market">
      <div class="photo" role="img" aria-label="Photo of a hand installing a white security camera" style="background:linear-gradient(135deg,#b98a5e 0%,#e9e8e6 45%,#f4f4f4 100%)"></div>
      <h3>Residential</h3><hr>
      <p>Let us assist you with your project!<br>No project is to big or small.</p>
    </div>
    <div class="market">
      <div class="photo" role="img" aria-label="Photo of a glass office tower seen from below" style="background:linear-gradient(160deg,#cfe1f2 0%,#4d7db8 45%,#1d3f73 75%,#7fa3cc 100%)"></div>
      <h3>Commercial</h3><hr>
      <p>Tessaridge is a leading services provider for Fortune 500 businesses with multiple locations.</p>
    </div>
    <div class="market">
      <div class="photo" role="img" aria-label="Photo of the domed capitol building under a blue sky" style="background:linear-gradient(180deg,#2f4f8f 0%,#6f8fbf 45%,#d9d6cf 70%,#8a8a86 100%)"></div>
      <h3>Federal</h3><hr>
      <p>We are a trusted provider for the U.S. Government with a proven past performance.</p>
    </div>
  </div>
  <span class="more">Click here to view all our markets</span>
</section>

<footer class="site-footer">
  <div class="foot-brand"><i></i>TESSARIDGE</div>
  <div class="foot-rule"></div>
  <div class="follow"><span>Follow Us:</span><i></i><i></i><i></i></div>
  <div class="fcol" style="left:564px">
    <h4>Quick Links</h4><div class="bar"></div>
    <ul class="links"><li>Home</li><li>Construction</li><li>Low Voltage</li><li>Markets</li><li>Our Team</li><li>Contact Us</li></ul>
  </div>
  <div class="fcol" style="left:864px">
    <h4>Contact Us</h4><div class="bar"></div>
    <ul class="contact">
      <li><b><svg width="12" height="12" viewBox="0 0 24 24"><path fill="#fff" d="M6.6 10.8a15 15 0 006.6 6.6l2.2-2.2c.3-.3.7-.4 1-.2 1.1.4 2.3.6 3.6.6.6 0 1 .4 1 1V20c0 .6-.4 1-1 1A17 17 0 013 4c0-.6.4-1 1-1h3.5c.6 0 1 .4 1 1 0 1.3.2 2.5.6 3.6.1.3 0 .7-.2 1z"/></svg></b>555 - 014 - 2290</li>
      <li><b><svg width="12" height="9" viewBox="0 0 24 18"><rect width="24" height="18" fill="#fff"/><path d="M0 0l12 9 12-9" stroke="#333" stroke-width="2" fill="none"/></svg></b>support@tessaridge.com</li>
      <li><b><svg width="11" height="14" viewBox="0 0 20 26"><path fill="#fff" d="M10 0a10 10 0 00-10 10c0 7 10 16 10 16s10-9 10-16A10 10 0 0010 0zm0 14a4 4 0 110-8 4 4 0 010 8z"/></svg></b>Maple Hollow, IL</li>
    </ul>
  </div>
  <div class="copy">Copyright © 2021 Tessaridge - All Rights Reserved</div>
</footer>

</body>
</html>
```